Web Design Project (Mente Lumo)

We are going to do a therapy template to a psychologist. The site already exists, adress: www.mentelumo.net. So, its a total redesign job. I'm from Brazil, the language is PT-BR, so I'm gonna translate what you think be necessary. You can use the current structure from the website as a base to the new design. Check this template to see what I usually like: http://www.layoutkestrel.com/demo/51907.html
Updates

I'm waiting for new creative designs. The 'structure' image is just for 'pb'.

Requirements
Must have
• We need a modern menu, it should use a cool font style and make some kind of effect and little noise when the user pass over with the mouse (FLASH/HTML 5). The main page must emphasize the fact that we offer online treatment, like a picture or frame saying "Online Treatment, click here". It must also show the therapist picture and her name. The colors need to pass a tranquility feeling. The clinic telephone must always be present, doesn't matter which page the user is. The website must adapt to any resolution above 1024x768, crossbrowsing and accept javascript (I'll use www.slotvira.com, so its necessary embed code)
Nice to have
• I would appreciate if there was some kind of slow background animation, passing behind the text using the transparency.
Should not have
• Can't take too long to load, and won't have news or blog

```html
<!DOCTYPE html>
<html lang="pt-BR">
<head>
<meta charset="utf-8">
<title>Mente Lumo – Artigos</title>
<link rel="stylesheet" href="https://fonts.googleapis.com/css2?family=Mulish:ital,wght@0,400;0,700;0,800;1,400;1,800&family=Ubuntu:wght@400;500&family=Arimo:wght@400;700&display=swap">
<style>
:root{
  --teal-dark:#1f4b58;
  --teal:#3d8596;
  --teal-light:#5aa3b2;
  --ribbon:#1f6e63;
  --hero:#d3dadb;
  --page:#dfe4e3;
  --ink:#2a2a2a;
  --muted:#7b8587;
  --red:#e4141b;
  --tab-red:#c0283a;
  --modal-blue:#3aa9d4;
  --modal-head:#8fb6c6;
  --link:#1b5aa8;
  --footer:#2d6878;
}
*{box-sizing:border-box;margin:0;padding:0}
html,body{width:1080px;height:1200px;overflow:hidden}
body{position:relative;background:var(--page);font-family:"Mulish",sans-serif;color:var(--ink)}
.abs{position:absolute}
/* header */
.topbar{left:0;top:0;width:1080px;height:32px;background:var(--teal-dark)}
.navband{left:0;top:32px;width:1080px;height:48px;background:linear-gradient(#4a93a4,#357c8d)}
.nav a{position:absolute;top:50px;font-family:"Ubuntu",sans-serif;font-size:12px;color:#cfe4e8;text-decoration:none;letter-spacing:.2px}
.nav .dot{position:absolute;top:53px;width:4px;height:4px;border-radius:50%;background:#a9cdd5}
.ribbon{left:764px;top:0;width:75px;height:100px}
.ribbon a{color:#e8f2ee!important}
.logo-badge{left:422px;top:4px;width:219px;height:101px}
.logo-name{left:422px;top:30px;width:219px;text-align:center;font-family:"Mulish",sans-serif;font-weight:800;font-size:24px;color:#3c8a8c}
/* hero */
.hero{left:0;top:80px;width:1080px;height:380px;background:linear-gradient(180deg,#c9d2d3,#dde3e3)}
.hero-art{left:607px;top:101px;width:262px;height:346px;border-radius:48% 46% 30% 40%;background:radial-gradient(circle at 55% 40%,#6f9ab0,#3f6a84 60%,rgba(60,100,120,0) 75%)}
.hero-kicker{left:196px;top:160px;font-style:italic;font-size:23px;color:#3e5d69;font-weight:400}
.hero-title{left:270px;top:193px;font-style:italic;font-weight:800;font-size:25px;color:#2c3337}
.hero-text{left:181px;top:248px;font-size:11px;line-height:22px;color:#545b5e}
/* articles section */
.section-title{left:146px;top:479px;font-weight:800;font-size:16px;color:#3a3f42}
.cat{font-family:"Ubuntu",sans-serif;font-size:11px;color:var(--tab-red);background:#e9eded;padding:4px 6px}
.rule{height:1px;background:#c8d0d0}
.art-title{left:151px;top:615px;font-weight:700;font-size:13px;color:#333}
.art-text{font-size:11px;line-height:22px;color:#8a9396}
.quote-box{left:144px;top:893px;width:791px;height:63px;border:1px solid #c7cfcf;background:#e5e9e9}
.quote-by{left:869px;top:937px;font-size:10px;color:#5b7a8a}
/* modal */
.modal-tab{left:233px;top:244px;width:125px;height:23px;background:#fff;font-family:"Ubuntu",sans-serif;font-weight:500;font-size:12px;text-align:center;line-height:24px;color:#222}
.modal{left:233px;top:267px;width:606px;height:702px;background:#fff;border-top:2px solid var(--red);border-bottom:2px solid var(--red);overflow:hidden}
.m-gray{left:0;top:0;width:606px;height:20px;background:#6f7b80}
.m-head{left:0;top:20px;width:606px;height:99px;background:repeating-linear-gradient(135deg,#8db3c3 0 6px,#94b9c8 6px 12px)}
.m-uni{left:80px;top:12px;color:#fff;font-family:"Ubuntu",sans-serif;font-weight:500;font-size:15px;line-height:14px}
.m-uni small{display:block;font-size:8px}
.m-site{left:77px;top:48px;color:#fff;font-family:"Ubuntu",sans-serif;font-weight:500;font-size:38px}
.m-side{left:0;top:119px;width:71px;height:583px;background:linear-gradient(#2b90c2,#38acd5)}
.m-menu{left:71px;top:119px;width:535px;height:26px;border-top:1px solid #cfd;font-family:"Ubuntu",sans-serif;font-size:12px}
.m-menu span{position:absolute;top:7px}
.m-strip{left:71px;top:145px;width:535px;height:25px;background:#e6e6e6}
.m-crumb{left:78px;top:174px;font-family:"Arimo",sans-serif;font-size:11px;color:#555;white-space:nowrap}
.m-crumb b{font-weight:400;color:var(--link)}
.m-body{left:93px;top:200px;width:513px;height:500px;overflow:hidden;font-family:"Arimo",sans-serif;white-space:nowrap}
.m-body h1{font-size:15.5px;color:#1c5b9c;font-weight:700;margin-top:4px}
.share{display:flex;gap:6px;margin:6px 0 3px}
.share i{display:inline-block;width:28px;height:14px;border:1px solid #c8c8c8;border-radius:2px;background:#eef2f6}
.share em{display:inline-block;width:14px;height:14px;border:1px solid #ccc;font-style:normal;font-size:8px;text-align:center;line-height:13px;color:#555;margin-right:20px}
.m-sub{font-size:12.5px;color:#666;font-weight:700}
.m-meta{font-size:8.5px;color:#666;line-height:16px}
.m-author{font-size:11px;font-weight:700;color:#222;line-height:16px;margin-top:8px}
.m-body p{font-size:10.3px;line-height:16px;color:#333;margin-top:16px}
.vscroll{left:855px;top:274px;width:2px;height:688px;background:#fff}
.vhandle{left:848px;top:629px;width:16px;height:50px;border-radius:8px;background:linear-gradient(90deg,#c40d12,#f0343a)}
.hscroll{left:233px;top:984px;width:463px;height:2px;background:#fff}
.hhandle{left:435px;top:978px;width:50px;height:15px;border-radius:8px;background:linear-gradient(#f0343a,#c40d12)}
.close{left:703px;top:969px;width:135px;height:33px;background:var(--red);color:#fff;font-family:"Ubuntu",sans-serif;font-size:13px;text-align:center;line-height:33px}
/* cta */
.cta{width:249px;height:48px;border:1px solid #c5cccc;background:#e2e6e6}
.cta-bar{position:absolute;left:10px;top:8px;width:229px;height:30px;border-radius:2px;color:#e9e9e9;font-size:12px;line-height:30px;padding-left:47px}
.cta-icon{position:absolute;left:3px;top:-3px;width:34px;height:36px;border-radius:3px}
.phone-tab{left:726px;top:1025px;width:190px;height:72px}
.phone-num{left:772px;top:1069px;font-family:"Ubuntu",sans-serif;font-size:18px;color:#e0eeed}
/* footer */
.footer{left:0;top:1097px;width:1080px;height:103px;background:var(--footer)}
.f-line{left:150px;top:1148px;width:785px;height:1px;background:#4e8795}
.f-text{width:1080px;left:0;text-align:center;font-style:italic;font-size:11px;color:#7fa9b3}
.f-copy{left:0;top:1158px;width:1080px;text-align:center;font-size:8px;color:#86aeb7}
</style>
</head>
<body>

<header>
  <div class="abs topbar"></div>
  <div class="abs navband"></div>
  <svg class="abs ribbon" viewBox="0 0 75 100" aria-hidden="true">
    <path d="M0 0H75V92L37 84 0 100Z" fill="#1f6e63"/>
    <path d="M4 0V90M71 0V86" stroke="#8ac6b4" stroke-dasharray="3 3" fill="none"/>
  </svg>
  <svg class="abs logo-badge" viewBox="0 0 219 101" aria-hidden="true">
    <path d="M10 30Q0 30 8 14 40 16 60 12 90 8 109 0 128 8 158 12 178 16 211 14 219 30 211 30 219 46 215 70 180 78 150 84 120 88 109 101 98 88 68 84 38 78 4 70 0 46 10 30Z" fill="#c7dadb" stroke="#9cc1c5" stroke-width="2"/>
  </svg>
  <div class="abs logo-name">Mente Lumo</div>
  <nav class="nav">
    <a style="left:137px">HOME</a><span class="dot" style="left:196px"></span>
    <a style="left:225px">SERVIÇOS</a><span class="dot" style="left:302px"></span>
    <a style="left:329px">INDICAÇÕES</a>
    <a style="left:661px">PERGUNTAS</a><span class="dot" style="left:751px"></span>
    <a style="left:778px;color:#e8f2ee">ARTIGOS</a><span class="dot" style="left:848px"></span>
    <a style="left:875px">CONTATO</a>
  </nav>
</header>

<section>
  <div class="abs hero"></div>
  <div class="abs hero-art" role="img" aria-label="Ilustração de cabeça humana com engrenagens"></div>
  <div class="abs hero-kicker">O que é a</div>
  <div class="abs hero-title">Terapia Cognitiva?</div>
  <div class="abs hero-text">A Terapia Cognitiva tem como método a interpretação de<br>processos<br>vida cotidiana<br>processam<br>pensamentos<br>nutri-los, e</div>
</section>

<section>
  <div class="abs section-title">ARTIGOS</div>
  <span class="abs cat" style="left:150px;top:523px">ENTREVISTAS</span>
  <div class="abs rule" style="left:150px;top:570px;width:780px"></div>
  <span class="abs cat" style="left:146px;top:592px;background:none">TEXTOS</span>
  <div class="abs art-title">Construindo Laços</div>
  <div class="abs art-text" style="left:151px;top:636px">As cobranças da<br>se sente cansado<br>intensamente as<br>natureza. Desfru<br>mundo fica muito<br>método a interpr<br>do processamento<br>reduzi-los ou rej</div>
  <div class="abs art-text" style="left:838px;top:636px;text-align:right;width:96px">indivíduo<br><br>contato com a<br>alizar o<br>em como<br>vêm depois<br>di-os,</div>
  <span class="abs cat" style="left:146px;top:855px;background:none">PENSAMENTOS</span>
  <div class="abs quote-box"></div>
  <div class="abs quote-by">- Aldo Brenner</div>
</section>

<div class="abs modal-tab">ENTREVISTAS</div>
<div class="abs modal">
  <div class="abs m-gray"></div>
  <div class="abs m-head">
    <div class="abs m-uni"><small>Universidade</small>Aurora</div>
    <div class="abs m-site">Vale Claro Online</div>
  </div>
  <div class="abs m-side"></div>
  <div class="abs m-menu">
    <span style="left:7px;color:#2a9fd8">NOTÍCIAS</span>
    <span style="left:86px;color:#2aa56a">VÍDEOS</span>
    <span style="left:150px;color:#e2405a">RÁDIO BRISA</span>
    <span style="left:250px;color:#e5b52a">FOTOS</span>
  </div>
  <div class="abs m-strip"></div>
  <div class="abs m-crumb">Você está aqui: <b>VCOnline</b> › <b>Notícias</b> › <b>Comportamento</b> › <b>2011</b> › <b>04</b> › Psicóloga ensina a lidar com medo, perdas e luto</div>
  <article class="abs m-body">
    <h1>Psicóloga ensina a lidar com medo, perdas e luto após tragédias</h1>
    <div class="share"><i></i><em>0</em><i style="width:56px"></i><em>0</em><i style="width:56px"></i><em>0</em></div>
    <div class="m-sub">Segundo a especialista, naturalidade e diálogo são fundamentais ao falar sobre a morte</div>
    <div class="m-meta">Publicado em 12/04/2011 17:56<br>Última atualização às 17:56</div>
    <div class="m-author">MARINA VELLOZO<br>Da Redação*</div>
    <p>A psicóloga, Lia Moreira Santana, explicou como lidar com o medo, perdas e luto após tragédias, em entrevista ao indivíduo<br>concedida ao VConline. E também incentiva os pais a dialogarem com os jovens que estão inseguros em ir à escola e<br>estudar com receio de acontecer a mesma coisa com eles e com pessoas próximas. Um exemplo é o massacre que vitimou<br>12 adolescentes em Realengo no Rio de Janeiro na última quinta-feira (7).</p>
    <p>A psicóloga comentou a importância de observar o comportamento das crianças. “Elas podem ficar assustadas e<br>medrosas, porque sentem tristeza por serem impotentes de ajudar, e acabam absorvendo o estresse dos adultos que<br>vivenciaram a situação. Essas crianças precisarão de mais amor, apoio e estrutura em sua rotina diária para se<br>recuperar deste trauma.”</p>
    <p>De acordo com a psicóloga, é importante conversar cuidadosamente com as crianças sobre crenças religiosas. Diante de<br>um episódio triste, elas podem desenvolver o medo ou ficarem ressentidas em relação a um Deus que levou embora<br>alguém amado e necessário.”</p>
    <p>As crianças precisam de uma explicação adequada sobre a causa da morte de algum parente ou amigo. É importante ter<br>uma pessoa em que ela confie e possua intimidade, que precisará de apoio nessa fase. “Quando o adulto dá respostas<br>vagos e tentam protegê-las da verdade com medo que sofram, isto apenas faz aumentar a confusão.</p>
    <p>Devem ser evitados termos que minimizem a morte, como ‘foi embora’, ou ‘está dormindo’. Quando se evita falar<br>sobre a morte ou quando é mantido o silêncio, indiretamente ensinamos a elas que a morte é um assunto proibido. É<br>importante falar com a maior naturalidade possível e não fugir do diálogo, nem mude de assunto. A morte faz parte</p>
  </article>
</div>
<div class="abs vscroll"></div>
<div class="abs vhandle"></div>
<div class="abs hscroll"></div>
<div class="abs hhandle"></div>
<div class="abs close">FECHAR</div>

<section>
  <div class="abs cta" style="left:148px;top:1034px">
    <div class="cta-bar" style="background:linear-gradient(#a9587a,#8e3f63)"><span style="font-style:italic">Agende online</span> seu atendimento
      <div class="cta-icon" style="background:#b8c2c8" role="img" aria-label="Ícone de calendário"></div></div>
  </div>
  <div class="abs cta" style="left:417px;top:1034px">
    <div class="cta-bar" style="background:linear-gradient(#2f6b8a,#1f4f6c)">Veja onde estamos
      <div class="cta-icon" style="background:#8fb2c0" role="img" aria-label="Miniatura de mapa da localização"></div></div>
  </div>
  <svg class="abs phone-tab" viewBox="0 0 190 72" aria-hidden="true">
    <path d="M0 72L165 0 190 72Z" fill="#2f8f8c"/>
    <path d="M12 42c2-3 5-3 6 0l2 4c1 2-1 3-2 4 2 4 5 7 9 9 1-1 2-3 4-2l4 2c3 1 3 4 0 6-3 2-7 2-12-2-6-5-10-11-11-16 0-2 0-4 0-5z" fill="#d02a2a"/>
  </svg>
  <div class="abs phone-num">(11) 5550-2047</div>
</section>

<footer>
  <div class="abs footer"></div>
  <div class="abs f-text" style="top:1108px">Rua das Acácias, 140, 5º andar, Sala 52 - Centro - Vila Serena, SP</div>
  <div class="abs f-text" style="top:1127px">
    <svg width="13" height="9" viewBox="0 0 13 9" style="vertical-align:middle;margin-right:8px" aria-hidden="true"><rect width="13" height="9" fill="#a9c58b"/><path d="M0 0l6.5 5L13 0" stroke="#6f9a55" fill="none"/></svg>contato@mentelumo.net</div>
  <div class="abs f-line"></div>
  <div class="abs f-copy">Copyright © 2012 - Todos os direitos reservados</div>
</footer>

</body>
</html>
```